6 Sizes Set - Static Banners

We have an html template for our newsletter which include graphic elements and we need images to populate these fixed Grey spaces.

Attachment 1: PLEASE READ FULL Graphic Brief is the complete brief describing all fine details.

Attachment 2: layout, shows the example of template

Attachment 3: We need the 6 image sizes (i.e. different fonts, backgrounds, colors, casino icons) – attached Styles Folder for an idea of the variety. These are just a few examples.

Target Market(s)

global

Industry/Entity Type

Casino

Requirements
Must have
• Refer to attach Full brief, for complete explanation
Nice to have
• Second Place: refer to Screenshot
Perfect example of what to submit

```html
<!DOCTYPE html>
<html lang="en">
<head>
<meta charset="utf-8">
<title>Casino Newsletter Banner Set</title>
<link rel="stylesheet" href="https://fonts.googleapis.com/css2?family=Anton&family=Open+Sans:wght@700&display=swap">
<style>
  :root {
    --bg: #000000;
    --frame: #8a8a8a;
    --headline: #fff21a;
    --headline-stroke: #000000;
    --btn-top: #ff7a1a;
    --btn-bottom: #e84a00;
    --btn-border: #2e9a2e;
    --btn-text: #ffffff;
    --coin: #ffe600;
    --coin-edge: #b89a00;
    --felt: #1f6b3a;
    --wood: #6b3b16;
  }
  * { box-sizing: border-box; margin: 0; padding: 0; }
  html, body { width: 1200px; height: 1029px; overflow: hidden; background: var(--bg); }
  .canvas { position: relative; width: 1200px; height: 1029px; background: var(--bg); }

  .banner {
    position: absolute;
    border: 3px solid var(--frame);
    overflow: hidden;
  }
  .banner__art { position: absolute; inset: 0; }
  .banner__pointer {
    position: absolute; bottom: 0; left: 50%;
    width: 0; height: 0;
    border-left: 12px solid transparent;
    border-right: 12px solid transparent;
    border-bottom: 12px solid #ffffff;
    transform: translateX(-50%);
  }
  .headline {
    position: absolute;
    font-family: "Anton", "Impact", sans-serif;
    color: var(--headline);
    text-transform: uppercase;
    line-height: 1;
    letter-spacing: 0.5px;
    -webkit-text-stroke: 2px var(--headline-stroke);
    paint-order: stroke fill;
    text-shadow: 3px 3px 0 var(--headline-stroke);
  }

  .banner--blackjack { left: 55px; top: 86px; width: 336px; height: 216px; }
  .banner--blackjack .banner__art { background: linear-gradient(135deg, var(--wood) 0%, #8a4a1c 30%, var(--felt) 55%, #2d8a4a 100%); }
  .banner--blackjack .headline--top { left: 0; right: 0; top: 14px; text-align: center; font-size: 58px; }
  .banner--blackjack .headline--bottom { left: 0; right: 0; bottom: 14px; text-align: center; font-size: 40px; text-transform: none; }

  .banner--vip { left: 442px; top: 122px; width: 130px; height: 168px; }
  .banner--vip .banner__art { background: linear-gradient(180deg, #3a0a0a 0%, #7a1a10 45%, #d8d8d8 70%, #f2f2f2 100%); }
  .banner--vip .headline--top { left: 0; right: 0; top: 22px; text-align: center; font-size: 50px; }
  .banner--vip .vip-band {
    position: absolute; left: 0; right: 0; top: 85px; height: 34px;
    background: #000; display: flex; align-items: center; justify-content: center;
    font-family: "Anton", "Impact", sans-serif; font-size: 19px; color: var(--headline); text-transform: uppercase;
  }

  .banner--cashback { left: 639px; top: 161px; width: 86px; height: 84px; }
  .banner--cashback .banner__art { background: linear-gradient(160deg, #5a5a5a 0%, #3a3a3a 60%, #2a2a2a 100%); }
  .banner--cashback .headline { left: 0; right: 0; text-align: center; -webkit-text-stroke: 1px #000; text-shadow: 1px 1px 0 #000; }
  .banner--cashback .headline--top { top: 36px; font-size: 19px; }
  .banner--cashback .headline--bottom { top: 56px; font-size: 12px; }

  .banner--jackpots { left: 789px; top: 96px; width: 350px; height: 235px; }
  .banner--jackpots .banner__art { background: linear-gradient(180deg, #1a1a1a 0%, #2a2a2a 55%, var(--felt) 78%, #2d8a4a 100%); }
  .banner--jackpots .headline { left: 0; right: 0; text-align: center; font-size: 56px; text-shadow: 0 0 14px #fff27a, 3px 3px 0 #000; }
  .banner--jackpots .headline--top { top: 66px; }
  .banner--jackpots .headline--bottom { top: 122px; }

  .banner--spins { left: 46px; top: 394px; width: 1106px; height: 161px; }
  .banner--spins .banner__art { background: linear-gradient(90deg, #4a4a42 0%, #6a6a5a 35%, #3a2a1a 60%, #7a2a1a 80%, #2a1a10 100%); }
  .banner--spins .headline { left: 40px; top: 38px; font-size: 80px; }

  .banner--rollers { left: 46px; top: 615px; width: 351px; height: 93px; }
  .banner--rollers .banner__art { background: linear-gradient(90deg, #2a1a14 0%, #5a3a28 40%, #8a2a1a 70%, #3a2a20 100%); }
  .banner--rollers .headline { left: 16px; top: 16px; font-size: 44px; color: #ffffff; font-style: italic; text-shadow: 2px 2px 0 #000; }

  .cta {
    position: absolute;
    display: flex; align-items: center; justify-content: space-between;
    padding: 0 8px 0 20px;
    height: 75px;
    border: 3px solid var(--btn-border);
    background: linear-gradient(180deg, var(--btn-top) 0%, var(--btn-bottom) 100%);
    font-family: "Open Sans", Arial, sans-serif; font-weight: 700;
    font-size: 29px; color: var(--btn-text);
    text-decoration: none;
  }
  .cta__icon { width: 58px; height: 58px; flex: none; }
  .cta--click { left: 881px; top: 636px; width: 257px; }
  .cta--play { left: 893px; top: 732px; width: 245px; }
  .cta--join { left: 890px; top: 821px; width: 249px; }
  .cta--join-now { left: 811px; top: 917px; width: 327px; }
</style>
</head>
<body>
<main class="canvas">

  <section class="banner banner--blackjack">
    <div class="banner__art" role="img" aria-label="Photo of a hand dealing cards on a green blackjack table with chips"></div>
    <h2 class="headline headline--top">Blackjack</h2>
    <p class="headline headline--bottom">Tournaments</p>
    <span class="banner__pointer"></span>
  </section>

  <section class="banner banner--vip">
    <div class="banner__art" role="img" aria-label="Red sparkling lights above playing cards"></div>
    <h2 class="headline headline--top">VIP</h2>
    <p class="vip-band">Rewards</p>
  </section>

  <section class="banner banner--cashback">
    <div class="banner__art" role="img" aria-label="Hand holding a fan of playing cards"></div>
    <h2 class="headline headline--top">Best</h2>
    <p class="headline headline--bottom">Cashbacks</p>
  </section>

  <section class="banner banner--jackpots">
    <div class="banner__art" role="img" aria-label="Photo of a smiling player pushing chips across a green casino table"></div>
    <h2 class="headline headline--top">Jackpots</h2>
    <p class="headline headline--bottom">Mania</p>
    <span class="banner__pointer"></span>
  </section>

  <section class="banner banner--spins">
    <div class="banner__art" role="img" aria-label="Close-up photo of a spinning roulette wheel"></div>
    <h2 class="headline">Free Spins Giveaway</h2>
    <span class="banner__pointer"></span>
  </section>

  <section class="banner banner--rollers">
    <div class="banner__art" role="img" aria-label="Dim photo of a casino floor with slot machines"></div>
    <h2 class="headline">High Rollers</h2>
    <span class="banner__pointer"></span>
  </section>

  <a class="cta cta--click" href="#">Click Here
    <svg class="cta__icon" viewBox="0 0 58 58" aria-hidden="true"><circle cx="29" cy="29" r="27" fill="var(--coin)" stroke="var(--coin-edge)" stroke-width="2"/><path d="M22 15 L42 29 L22 43 Z" fill="#000"/></svg>
  </a>
  <a class="cta cta--play" href="#">Play Now
    <svg class="cta__icon" viewBox="0 0 58 58" aria-hidden="true"><circle cx="29" cy="29" r="27" fill="var(--coin)" stroke="var(--coin-edge)" stroke-width="2"/><path d="M22 15 L42 29 L22 43 Z" fill="#000"/></svg>
  </a>
  <a class="cta cta--join" href="#">Join Free
    <svg class="cta__icon" viewBox="0 0 58 58" aria-hidden="true"><circle cx="29" cy="29" r="27" fill="var(--coin)" stroke="var(--coin-edge)" stroke-width="2"/><path d="M22 15 L42 29 L22 43 Z" fill="#000"/></svg>
  </a>
  <a class="cta cta--join-now" href="#">Join Here Now
    <svg class="cta__icon" viewBox="0 0 58 58" aria-hidden="true"><circle cx="29" cy="29" r="27" fill="var(--coin)" stroke="var(--coin-edge)" stroke-width="2"/><path d="M22 15 L42 29 L22 43 Z" fill="#000"/></svg>
  </a>

</main>
</body>
</html>
```